VELMAR, an e-commerce website with a twist, providing consumer-to-consumer and business-to-consumer sa

I have only uploaded 10 wire-frame pages of the website. These pages have been chosen for the different lay-outs and should give an idea of what will be needed. There are many more that I won’t upload yet, I aim to choose a winner first then there will be a high possibility that the winner will get the chance to do the design work for these later.
The design I have in mind is to keep it clean and easy with no/minimal fancy fonts and hieroglyphics. The logo is white with an orange highlight on a solid background of black, please note that the logo is white on a black background and is not a black box with white lettering, trust that makes sense. I like the idea of the top part of the website being black all the way across. I don’t see the need for more than 3 colours in the actual base website (the pictures and adverts added by users will add other colours). Although orange is the highlight colour in the logo I am open to suggestions on this, so long as the highlight colour features throughout the site.

Website width is 1220px, all pages in the PDF are 1220px

Logo font is Rezlong

The company is going to be like tradu, but much more focused on raising money for charity and humanitarian relief.

Target Market(s)

the modern era of smartphones and the sharing community

Industry/Entity Type

Business

Number of Pages Required

5+ page

Font styles to use
Sans Serif
Other font styles liked:
• rezlong

Colors
faa54b
f78f20
ffffff
000000
fbfbfb
f5f5f5

Requirements
Nice to have
• Although orange is the highlight colour in the logo I am open to suggestions on this, so long as the highlight colour features throughout the site.

```html
<!DOCTYPE html>
<html lang="en">
<head>
<meta charset="utf-8">
<title>VELMAR – Buy, Sell, Give</title>
<link rel="stylesheet" href="https://fonts.googleapis.com/css2?family=Roboto:wght@400;500;700&display=swap">
<style>
:root{
  --orange:#f78f20;
  --orange-soft:#faa54b;
  --red-orange:#f2532d;
  --black:#000;
  --white:#fff;
  --off:#fbfbfb;
  --panel:#f5f5f5;
  --card:#ebebeb;
  --line:#dcdcdc;
  --text:#333;
  --muted:#777;
  --footer:#3f3f3f;
  --footer-dark:#2a2a2a;
}
*{box-sizing:border-box;margin:0;padding:0}
html,body{width:1200px;height:2927px;overflow:hidden}
body{position:relative;background:var(--white);font-family:"Roboto",Arial,sans-serif;color:var(--text)}
.abs{position:absolute}
.topbar{left:0;top:0;width:1200px;height:29px;background:#e9e9e9;font-size:11px;color:#444}
.topbar span{position:absolute;top:8px}
.header{left:0;top:29px;width:1200px;height:88px;background:var(--black);color:var(--white)}
.logo{font-weight:500;font-size:46px;letter-spacing:-1px;color:var(--white);line-height:1}
.search{left:256px;top:35px;width:583px;height:34px;border-radius:17px;background:var(--white);font-size:11px;color:#333;padding:10px 20px}
.header-link{font-size:11px;top:53px}
.card-shadow{background:var(--white);border:1px solid #e6e6e6;box-shadow:0 1px 3px rgba(0,0,0,.08)}
.field{left:426px;width:254px;height:36px;border:1px solid #cfcfcf;font-size:11px;color:#666;padding:11px 14px;background:var(--white)}
.btn{background:var(--orange);color:var(--white);border-radius:20px;font-size:13px;text-align:center}
.cause h4{font-size:15px;font-weight:500;color:#333;margin-bottom:4px}
.cause p{font-size:11px;line-height:15px;color:#666}
.photo{display:block}
.section-title{font-size:24px;font-weight:500;color:var(--orange);text-align:center;width:1200px;left:0}
.testi{background:var(--card);box-shadow:0 2px 4px rgba(0,0,0,.15);text-align:center;padding:58px 30px 0}
.testi p{font-size:12px;line-height:17px;color:#666}
.testi h5{font-size:12px;font-weight:700;color:#222;margin-top:14px}
.testi small{font-size:11px;color:#777}
.avatar{width:70px;height:70px;border-radius:50%;border:4px solid var(--white);background:linear-gradient(#9a8f86,#4f5560)}
.partner{font-size:19px;font-weight:700;color:#234c8e;width:170px;line-height:1.15}
.promo h3{font-size:20px;font-weight:500;color:var(--white)}
.promo p{font-size:12px;color:var(--white);margin-top:12px}
.footer{left:0;top:2530px;width:1200px;height:338px;background:var(--footer);color:var(--white)}
.footer h6{font-size:18px;font-weight:500;letter-spacing:.5px}
.footer p{font-size:12px;line-height:17px}
.legal{left:0;top:2868px;width:1200px;height:59px;background:var(--footer-dark);color:#ccc;font-size:11px;padding:22px 0 0 135px}
</style>
</head>
<body>

<div class="abs topbar">
  <span style="left:73px">Notifications</span><span style="left:154px">|</span>
  <span style="left:168px">News</span><span style="left:212px">|</span>
  <span style="left:226px">List Item</span>
  <span style="left:930px">Notifications</span><span style="left:1006px">|</span>
  <span style="left:1022px">News</span><span style="left:1064px">|</span>
  <span style="left:1078px">List Item</span>
</div>

<header class="abs header">
  <div class="abs logo" style="left:74px;top:20px">velmar</div>
  <div class="abs search">Search
    <svg class="abs" style="right:14px;top:10px" width="14" height="14" viewBox="0 0 14 14"><circle cx="6" cy="6" r="4.5" fill="none" stroke="#222" stroke-width="2"/><line x1="9.3" y1="9.3" x2="13" y2="13" stroke="#222" stroke-width="2"/></svg>
  </div>
  <svg class="abs" style="left:1082px;top:14px" width="36" height="20" viewBox="0 0 36 20"><circle cx="10" cy="10" r="9" fill="#fff"/><circle cx="10" cy="8" r="3" fill="#000"/><path d="M4.5 15a6 4 0 0 1 11 0z" fill="#000"/><path d="M25 8l4 4 4-4" fill="none" stroke="#fff" stroke-width="1.6"/></svg>
  <span class="abs header-link" style="left:890px">Wish List</span>
  <svg class="abs" style="left:943px;top:53px" width="13" height="12" viewBox="0 0 13 12"><path d="M6.5 11L1.3 5.8A3 3 0 0 1 6.5 2a3 3 0 0 1 5.2 3.8z" fill="#fff"/></svg>
  <span class="abs header-link" style="left:985px">Shopping Basket</span>
  <svg class="abs" style="left:1087px;top:50px" width="20" height="16" viewBox="0 0 20 16"><path d="M1 5h18l-2.5 10h-13z" fill="#fff"/><path d="M6 5l4-4 4 4" fill="none" stroke="#fff" stroke-width="1.6"/></svg>
  <span class="abs header-link" style="left:1118px">0</span>
</header>

<!-- Top: videos, search, causes -->
<section>
  <div class="abs photo" role="img" aria-label="Video thumbnail: group of smiling young volunteers" style="left:70px;top:148px;width:330px;height:174px;background:linear-gradient(135deg,#8b7a6c,#c9b6a2 50%,#5f6f7c)"></div>
  <svg class="abs" style="left:213px;top:203px" width="56" height="56" viewBox="0 0 56 56"><circle cx="28" cy="28" r="27" fill="#fff"/><circle cx="28" cy="28" r="22" fill="#000"/><path d="M23 18l14 10-14 10z" fill="#fff"/></svg>
  <div class="abs photo" role="img" aria-label="Video: hands sharing food among children" style="left:70px;top:343px;width:330px;height:170px;background:linear-gradient(135deg,#5a3a26,#b27a45 55%,#3a2a20)"></div>
  <svg class="abs" style="left:210px;top:386px" width="56" height="56" viewBox="0 0 56 56"><circle cx="28" cy="28" r="27" fill="#fff"/><circle cx="28" cy="28" r="22" fill="#000"/><path d="M23 18l14 10-14 10z" fill="#fff"/></svg>
  <div class="abs" style="left:70px;top:483px;width:330px;height:30px;background:rgba(0,0,0,.75)"></div>
  <svg class="abs" style="left:78px;top:490px" width="316" height="16" viewBox="0 0 316 16"><circle cx="8" cy="8" r="7" fill="#fff"/><path d="M6 5l5 3-5 3z" fill="#000"/><rect x="24" y="7" width="220" height="2" fill="#888"/><rect x="24" y="7" width="70" height="2" fill="#fff"/><path d="M268 5h3l4-3v12l-4-3h-3z" fill="#fff"/><path d="M295 3h5M295 3v5M311 13h-5M311 13v-5" stroke="#fff" stroke-width="1.6" fill="none"/></svg>

  <div class="abs" style="left:411px;top:117px;width:1px;height:435px;background:var(--line)"></div>
  <div class="abs" style="left:696px;top:117px;width:1px;height:435px;background:var(--line)"></div>
  <div class="abs" style="left:426px;top:146px;font-size:15px;font-weight:500;color:var(--orange)">Search For Causes</div>
  <div class="abs field" style="top:186px">Item</div>
  <div class="abs field" style="top:240px">Location</div>
  <div class="abs field" style="top:293px">From</div>
  <div class="abs field" style="top:347px">To</div>
  <div class="abs btn" style="left:429px;top:404px;width:246px;height:34px;padding-top:9px">Search</div>

  <div class="abs card-shadow cause" style="left:714px;top:150px;width:421px;height:95px">
    <div class="abs" role="img" aria-label="Donation jar with coins" style="left:2px;top:2px;width:126px;height:89px;background:linear-gradient(#b7b2a8,#6e6456)"></div>
    <div class="abs" style="left:134px;top:6px;width:275px"><h4>Donate</h4><p>Nullam quis quam ac orci accumsan tincidunt. Curabitur lacinia nibh eu dapibus efficitu dapibus.</p></div>
  </div>
  <div class="abs card-shadow cause" style="left:714px;top:275px;width:421px;height:95px">
    <div class="abs" role="img" aria-label="Children standing together in a village" style="left:2px;top:2px;width:126px;height:89px;background:linear-gradient(#7a5a45,#3f2c22)"></div>
    <div class="abs" style="left:134px;top:6px;width:275px"><h4>Lorem ipsum dolor</h4><p>Nullam quis quam ac orci accumsan tincidunt. Curabitur lacinia nibh eu dapibus efficitu dapibus.</p></div>
  </div>
  <div class="abs card-shadow cause" style="left:714px;top:400px;width:421px;height:95px">
    <div class="abs" role="img" aria-label="Hands holding empty bowls" style="left:2px;top:2px;width:126px;height:89px;background:linear-gradient(#6d6a66,#2f2d2b)"></div>
    <div class="abs" style="left:134px;top:6px;width:275px"><h4>Lorem ipsum dolor</h4><p>Nullam quis quam ac orci accumsan tincidunt. Curabitur lacinia nibh eu dapibus efficitu dapibus.</p></div>
  </div>
</section>

<!-- Hero -->
<section class="abs" role="img" aria-label="Smiling young man in a checked shirt holding a charity collection tin on a sunny street" style="left:0;top:552px;width:1200px;height:488px;background:linear-gradient(90deg,#6f8a62 0%,#b9a48c 35%,#d9cbb8 55%,#8aa1c4 75%,#d5d2cc 100%)"></section>
<div class="abs" style="left:74px;top:552px;width:464px;height:164px;background:var(--red-orange);color:var(--white);padding:14px 0 0 60px">
  <div style="font-size:38px;line-height:1">How we work with</div>
  <div style="font-size:76px;line-height:1.05">Charities</div>
</div>

<!-- Testimonials -->
<div class="abs section-title" style="top:1092px">Testimonials</div>
<div class="abs" style="left:0;top:1135px;width:1200px;text-align:center;font-size:12px;color:#444">Lorem ipsum is a dummy text it will use for subtitle here</div>
<svg class="abs" style="left:97px;top:1316px" width="14" height="24" viewBox="0 0 14 24"><path d="M12 2L3 12l9 10" fill="none" stroke="var(--orange)" stroke-width="3"/></svg>
<svg class="abs" style="left:1086px;top:1316px" width="14" height="24" viewBox="0 0 14 24"><path d="M2 2l9 10-9 10" fill="none" stroke="var(--orange)" stroke-width="3"/></svg>

<div class="abs testi" style="left:150px;top:1216px;width:287px;height:218px"><p>Maecenas commodo nisi nibh, vel suscipit diam gravida sed. Cras finibus leo vel mauris lacinia pulvinar.Maecenas placerat, leo sed bibendum laoreet</p><h5>ADRIAN HOLT</h5><small>Director</small></div>
<div class="abs testi" style="left:458px;top:1216px;width:289px;height:218px"><p>Maecenas commodo nisi nibh, vel suscipit diam gravida sed. Cras finibus leo vel mauris lacinia pulvinar.Maecenas placerat, leo sed bibendum laoreet</p><h5>BIANCA REYES</h5><small>Director</small></div>
<div class="abs testi" style="left:767px;top:1216px;width:288px;height:218px"><p>Maecenas commodo nisi nibh, vel suscipit diam gravida sed. Cras finibus leo vel mauris lacinia pulvinar.Maecenas placerat, leo sed bibendum laoreet</p><h5>SELMA NORRIS</h5><small>Director</small></div>
<div class="abs avatar" role="img" aria-label="Portrait of the reviewer" style="left:263px;top:1180px"></div>
<div class="abs avatar" role="img" aria-label="Portrait of the reviewer" style="left:572px;top:1180px"></div>
<div class="abs avatar" role="img" aria-label="Portrait of the reviewer" style="left:881px;top:1180px"></div>
<svg class="abs" style="left:574px;top:1455px" width="52" height="12" viewBox="0 0 52 12"><circle cx="6" cy="6" r="5" fill="var(--orange)"/><circle cx="26" cy="6" r="5" fill="#333"/><circle cx="46" cy="6" r="5" fill="#333"/></svg>

<!-- Help band -->
<section class="abs" role="img" aria-label="Smiling child leaning on a wooden desk in a dim classroom" style="left:0;top:1535px;width:1200px;height:490px;background:radial-gradient(ellipse at 30% 45%,#6b4f34 0%,#3a2a1d 45%,#1e1812 100%)"></section>
<div class="abs" style="left:653px;top:1640px;width:420px;color:var(--white)">
  <div style="font-size:28px;font-weight:500">We need your Help</div>
  <div style="font-size:13px;font-weight:500;color:var(--orange);margin-top:18px">Let's Stop This hunger and fulfill their happiness</div>
  <p style="font-size:12px;line-height:19px;margin-top:12px;color:#eee">Donec iaculis ligula ac ultricies venenatis. Duis augue diam, dapibus nec quam in, ullamcorper convallis dolor. Aliquam erat volutpat. Aenean euismod sapien id lacus cursus porta. Nunc pellentesque at diam id suscipit.</p>
</div>
<div class="abs btn" style="left:657px;top:1824px;width:186px;height:49px;border-radius:25px;padding:15px 60px 0 0">Learn More</div>
<svg class="abs" style="left:802px;top:1835px" width="28" height="28" viewBox="0 0 28 28"><circle cx="14" cy="14" r="13" fill="#fff"/><path d="M11 8l7 6-7 6z" fill="var(--orange)"/></svg>

<!-- Charities -->
<div class="abs" style="left:72px;top:2070px;font-size:24px;font-weight:500;color:#444">Charities Supported</div>
<div class="abs partner" style="left:76px;top:2150px">Northgate Mutual</div>
<div class="abs partner" style="left:250px;top:2150px">Forwardline</div>
<div class="abs partner" style="left:438px;top:2150px">Safehaven Cover</div>
<div class="abs partner" style="left:76px;top:2236px">Mercer Vale Group</div>
<div class="abs partner" style="left:260px;top:2226px">Coastal Aid Plan</div>
<div class="abs partner" style="left:436px;top:2236px">Arrowpoint Exchange</div>
<div class="abs partner" style="left:72px;top:2322px">Corvid Group</div>
<div class="abs partner" style="left:258px;top:2328px">Silver Hawk Cover</div>
<div class="abs partner" style="left:422px;top:2318px">Emberline Fund</div>
<div class="abs partner" style="left:72px;top:2426px">Wayfarers</div>
<div class="abs partner" style="left:256px;top:2418px">Terravia</div>
<div class="abs partner" style="left:462px;top:2410px">Civic Relief Fund</div>

<div class="abs promo" role="img" aria-label="Young girl smiling among a crowd" style="left:620px;top:2138px;width:508px;height:156px;background:linear-gradient(90deg,#1e1a17 0%,#4a382a 55%,#8a6a4e 100%)"></div>
<div class="abs promo" style="left:634px;top:2158px"><h3>WE NEED YOUR SUPPORT TO</h3><p>Accommodate, Feed And Educate.</p></div>
<div class="abs btn" style="left:638px;top:2230px;width:110px;height:30px;font-size:11px;padding:8px 28px 0 0">Donate Now!</div>
<svg class="abs" style="left:724px;top:2236px" width="18" height="18" viewBox="0 0 18 18"><circle cx="9" cy="9" r="8" fill="#fff"/><path d="M7 5l5 4-5 4z" fill="var(--orange)"/></svg>

<div class="abs promo" role="img" aria-label="Volunteers serving food to people in need" style="left:620px;top:2314px;width:508px;height:156px;background:linear-gradient(90deg,#1c1c1c 0%,#4b4843 55%,#8a8378 100%)"></div>
<div class="abs promo" style="left:634px;top:2332px"><h3>Major Challenges</h3><p>We can Tackle together.</p></div>
<div class="abs btn" style="left:638px;top:2398px;width:110px;height:30px;font-size:11px;padding:8px 28px 0 0">Donate Now!</div>
<svg class="abs" style="left:724px;top:2404px" width="18" height="18" viewBox="0 0 18 18"><circle cx="9" cy="9" r="8" fill="#fff"/><path d="M7 5l5 4-5 4z" fill="var(--orange)"/></svg>

<!-- Footer -->
<footer class="abs footer">
  <div class="abs logo" style="left:133px;top:94px">velmar</div>
  <p class="abs" style="left:133px;top:148px;width:240px">Street 238,52 tempor Donec ultricies id porttitor. Vestibulum ante.</p>
  <p class="abs" style="left:133px;top:224px"><span style="color:var(--orange)">Phone:</span>&nbsp;&nbsp;&nbsp;200 555 0147</p>
  <p class="abs" style="left:133px;top:257px"><span style="color:var(--orange)">Email:</span>&nbsp;&nbsp;&nbsp;hello@velmar.org</p>
  <div class="abs" style="left:420px;top:80px;width:1px;height:210px;background:#555"></div>
  <div class="abs" style="left:771px;top:80px;width:1px;height:210px;background:#555"></div>

  <h6 class="abs" style="left:482px;top:80px">RECENT POSTS</h6>
  <div class="abs" role="img" aria-label="Post thumbnail: hands writing" style="left:482px;top:124px;width:78px;height:66px;background:linear-gradient(#8a7a66,#3c342b)"></div>
  <p class="abs" style="left:566px;top:120px;width:180px">Aliquam et varius orci, ut ornare justo. Lorem ipsum dolor sit amet.<br><span style="color:var(--orange);font-size:11px">charity</span> <span style="font-size:11px">| Dec-3-2017</span></p>
  <div class="abs" role="img" aria-label="Post thumbnail: man reading" style="left:482px;top:225px;width:78px;height:66px;background:linear-gradient(#7a6e62,#2f2a25)"></div>
  <p class="abs" style="left:566px;top:222px;width:180px">Aliquam et varius orci, ut ornare justo. Lorem ipsum dolor sit amet.<br><span style="color:var(--orange);font-size:11px">charity</span> <span style="font-size:11px">| Dec-3-2017</span></p>

  <h6 class="abs" style="left:819px;top:80px">NEWSLETTER SIGNUP</h6>
  <p class="abs" style="left:819px;top:125px">Street tempor Donec ultricies mattis nulla.</p>
  <div class="abs" style="left:819px;top:160px;width:166px;height:35px;background:var(--white);color:#999;font-size:11px;padding:11px 10px">Email Addresss</div>
  <div class="abs" style="left:985px;top:160px;width:86px;height:35px;background:var(--orange);font-size:11px;font-weight:500;text-align:center;padding-top:11px">SIGNUP</div>
  <p class="abs" style="left:819px;top:226px;font-size:11px;font-weight:500">FOLLOW US</p>
  <svg class="abs" style="left:819px;top:258px" width="210" height="14" viewBox="0 0 210 14" role="img" aria-label="Social links">
    <circle cx="6" cy="7" r="5" fill="#fff"/><circle cx="36" cy="7" r="5" fill="#fff"/><circle cx="66" cy="7" r="5" fill="#fff"/><circle cx="96" cy="7" r="5" fill="#fff"/><circle cx="126" cy="7" r="5" fill="#fff"/><circle cx="156" cy="7" r="5" fill="#fff"/><circle cx="186" cy="7" r="5" fill="#fff"/>
  </svg>
</footer>
<div class="abs legal">© Copyright <span style="color:var(--orange)">velmar</span> 2017 All Rights Reserved</div>

</body>
</html>
```